Brightway Dwelling & Yard Care - Maintenance & Improvements

Handyman service - Total home improvement and maintenance

We do everything indoors, ie. carpentry, and outdoors, ie. garden maintenance

No job too small or too unusual

7 Days per week
Updates

I want the overall impression not to favour either gender ... eg. maybe don't use the word Handy'man' because we also have a Fixmistress service .... but just stay with a generic theme of home improvement and maintenance

Industry/Entity Type

Home Improvement

Contact Information for Business Card

Brightway Dwelling & Yard Care
7 Days per Week
Total Home Maintenance and Improvements
Handyman | Fixmistress | Our (DIY) Task Pal
Ph: 0487 613 902
www.brightwaydwellingyard.com.au

Requirements
Must have
• The black and white image of various workers, as per attached

```html
<!DOCTYPE html>
<html lang="en">
<head>
<meta charset="utf-8">
<title>Brightway Dwelling &amp; Yard Care – Business Cards</title>
<link href="https://fonts.googleapis.com/css2?family=Tinos:wght@700&family=Didact+Gothic&display=swap" rel="stylesheet">
<style>
  :root {
    --page: #eeeeec;
    --paper: #ffffff;
    --ink: #111111;
    --blue: #1e86e8;
    --white: #ffffff;
    --figure-dark: #bfbfbf;
    --figure-blue: #cfe6fb;
  }
  * { box-sizing: border-box; margin: 0; padding: 0; }
  html, body {
    width: 1200px;
    height: 900px;
    overflow: hidden;
    background: var(--page);
  }
  .canvas {
    position: relative;
    width: 1200px;
    height: 900px;
    display: flex;
    flex-direction: column;
    align-items: center;
    justify-content: center;
    gap: 40px;
  }
  .card {
    position: relative;
    width: 700px;
    height: 400px;
    background: var(--paper);
    box-shadow: 0 6px 18px rgba(0,0,0,0.18);
    overflow: hidden;
    font-family: "Didact Gothic", "Century Gothic", sans-serif;
  }
  .card__head {
    height: 150px;
    padding: 28px 0 0 110px;
  }
  .brand-name {
    font-family: "Tinos", "Times New Roman", serif;
    font-weight: 700;
    font-size: 36px;
    letter-spacing: 0.5px;
    color: var(--ink);
    line-height: 1;
  }
  .tagline {
    text-align: center;
    font-size: 19px;
    line-height: 1.45;
    letter-spacing: 0.4px;
  }
  .card__band {
    position: absolute;
    left: 0; right: 0; bottom: 0;
    top: 150px;
    padding: 0 28px;
  }
  .workers {
    height: 80px;
    margin-top: 18px;
    border-radius: 4px;
  }
  .rule {
    height: 3px;
    margin-top: 8px;
    background: var(--white);
  }
  .contact {
    margin-top: 14px;
    text-align: center;
    color: var(--white);
    font-size: 20px;
    line-height: 1.5;
    letter-spacing: 0.6px;
  }

  /* Black edition */
  .card--mono .card__head { height: 175px; }
  .card--mono .tagline { color: var(--ink); margin-top: 16px; }
  .card--mono .card__band { top: 190px; background: var(--ink); }
  .card--mono .workers { background: linear-gradient(90deg, #2a2a2a, var(--figure-dark) 50%, #2a2a2a); opacity: 0.55; margin-top: 14px; }

  /* Blue edition */
  .card--blue .tagline { color: var(--blue); margin-top: 12px; }
  .card--blue .card__band { top: 180px; background: var(--blue); }
  .card--blue .workers { background: linear-gradient(90deg, #3f98ec, var(--figure-blue) 50%, #3f98ec); opacity: 0.6; margin-top: 16px; }
  .card--blue .contact { color: var(--ink); }
  .card--blue .contact .web { color: var(--white); }
  .card--blue .card__head { height: 180px; }
</style>
</head>
<body>
<main class="canvas">

  <section class="card card--mono" aria-label="Business card, black edition">
    <header class="card__head">
      <h1 class="brand-name">Brightway Dwelling &amp; Yard Care</h1>
      <p class="tagline">7 Days per Week Total Home Maintenance &amp; Improvements<br>Handyman | Fixmistress</p>
    </header>
    <div class="card__band">
      <div class="workers" role="img" aria-label="Row of white silhouette figures doing carpentry, painting, gardening, mowing, plumbing and watering"></div>
      <div class="rule"></div>
      <p class="contact">Our (DIY) Task Pal &nbsp;Ph: 0487 613 902<br>www.brightwaydwellingyard.com.au</p>
    </div>
  </section>

  <section class="card card--blue" aria-label="Business card, blue edition">
    <header class="card__head">
      <h1 class="brand-name">Brightway Dwelling &amp; Yard Care</h1>
      <p class="tagline">7 Days per Week Total Home Maintenance &amp; Improvements<br>Handyman | Fixmistress</p>
    </header>
    <div class="card__band">
      <div class="workers" role="img" aria-label="Row of white silhouette figures doing carpentry, painting, gardening, mowing, plumbing and watering"></div>
      <div class="rule"></div>
      <p class="contact">Our (DIY) Task Pal &nbsp;Ph: 0487 613 902<br><span class="web">www.brightwaydwellingyard.com.au</span></p>
    </div>
  </section>

</main>
</body>
</html>
```